Horticulture Consulting Company Premium Card

We are looking for new design for a premium business card.
Our cards will be printed on glossy and embossed premium card stock.

Target Market(s)

Horticulture business owners needing our consulting services

Contact Information for Business Card

Marcus Thorne
(555) 348-2916
Marcus@velturaq.com

Requirements
Must have
• Company Logo and Contact information.
• Some additional work to add interest to the card
Should not have
• Red or Yellow

```html
<!DOCTYPE html>
<html lang="en">
<head>
<meta charset="utf-8">
<title>Velturaq Business Card</title>
<link rel="stylesheet" href="https://fonts.googleapis.com/css2?family=Montserrat:wght@600;800&family=Quicksand:wght@500&display=swap">
<style>
  :root {
    --backdrop: #e8ebe5;
    --card: #f7f7f3;
    --green: #2f9a3c;
    --blue: #1f4b9f;
    --ink: #4a4a4a;
    --shadow: rgba(0, 0, 0, 0.16);
  }
  * { margin: 0; padding: 0; box-sizing: border-box; }
  html, body {
    width: 1200px;
    height: 1050px;
    overflow: hidden;
    background: var(--backdrop);
  }
  .canvas {
    position: relative;
    width: 1200px;
    height: 1050px;
  }
  .card {
    position: absolute;
    left: 290px;
    width: 620px;
    height: 355px;
    background: var(--card);
    overflow: hidden;
    box-shadow: 0 10px 28px var(--shadow);
  }
  .card--front { top: 120px; }
  .card--back { top: 575px; }

  /* front */
  .brand {
    position: absolute;
    left: 40px;
    top: 38px;
    display: flex;
    align-items: center;
    gap: 12px;
  }
  .brand__dot {
    width: 44px;
    height: 44px;
    border-radius: 50%;
    background: var(--green);
  }
  .brand__name {
    font-family: "Montserrat", sans-serif;
    font-weight: 800;
    font-size: 30px;
    letter-spacing: 1px;
    color: var(--blue);
    line-height: 1;
  }
  .brand__tagline {
    position: absolute;
    left: 96px;
    top: 88px;
    font-family: "Montserrat", sans-serif;
    font-weight: 600;
    font-size: 9px;
    letter-spacing: 0.6px;
    color: var(--green);
    border-top: 1.5px solid var(--green);
    padding-top: 3px;
  }
  .person {
    position: absolute;
    left: 40px;
    top: 128px;
    font-family: "Montserrat", sans-serif;
    font-weight: 800;
    font-size: 20px;
    letter-spacing: 0.5px;
    color: var(--blue);
  }
  .contacts {
    position: absolute;
    left: 40px;
    top: 188px;
    list-style: none;
  }
  .contacts__item {
    display: flex;
    align-items: center;
    gap: 12px;
    margin-bottom: 12px;
    font-family: "Quicksand", sans-serif;
    font-weight: 500;
    font-size: 17px;
    color: var(--ink);
  }
  .contacts__icon {
    width: 18px;
    height: 18px;
    flex: none;
  }
  .edge-band {
    position: absolute;
    left: 0;
    top: 112px;
    width: 8px;
    height: 40px;
    background: var(--blue);
  }
  .accent-circle {
    position: absolute;
    right: -70px;
    bottom: -80px;
    width: 300px;
    height: 300px;
    border-radius: 50%;
    background: var(--green);
  }
  .accent-tab {
    position: absolute;
    right: 0;
    top: 150px;
    width: 40px;
    height: 22px;
    background: var(--blue);
  }

  /* back */
  .back-ring {
    position: absolute;
    left: -150px;
    top: -60px;
    width: 300px;
    height: 300px;
    border-radius: 50%;
    border: 26px solid var(--blue);
  }
  .back-brand {
    position: absolute;
    left: 220px;
    top: 140px;
    width: 360px;
    text-align: center;
  }
  .back-brand__name {
    font-family: "Montserrat", sans-serif;
    font-weight: 800;
    font-size: 52px;
    letter-spacing: 2px;
    color: var(--blue);
    line-height: 1;
  }
  .back-brand__tagline {
    margin-top: 10px;
    font-family: "Montserrat", sans-serif;
    font-weight: 600;
    font-size: 11px;
    letter-spacing: 0.8px;
    color: var(--green);
    border-top: 2px solid var(--green);
    border-bottom: 2px solid var(--green);
    padding: 4px 0;
  }
</style>
</head>
<body>
<main class="canvas">

  <section class="card card--front" aria-label="Card front">
    <div class="edge-band"></div>
    <div class="brand">
      <span class="brand__dot"></span>
      <span class="brand__name">VELTURAQ</span>
    </div>
    <p class="brand__tagline">CONTROLLED ENVIRONMENT AGRICULTURE</p>

    <h1 class="person">MARCUS THORNE</h1>

    <ul class="contacts">
      <li class="contacts__item">
        <svg class="contacts__icon" viewBox="0 0 18 18" aria-hidden="true">
          <circle cx="9" cy="9" r="9" fill="var(--green)"/>
          <path d="M6 4.5l1.6 2.2-1 1.1a6 6 0 0 0 3.6 3.6l1.1-1 2.2 1.6-.9 1.6C9.5 13.4 4.6 8.5 4.4 5.4z" fill="#fff"/>
        </svg>
        (555) 348-2916
      </li>
      <li class="contacts__item">
        <svg class="contacts__icon" viewBox="0 0 18 18" aria-hidden="true">
          <circle cx="9" cy="9" r="9" fill="var(--green)"/>
          <rect x="4.5" y="6" width="9" height="6.5" fill="#fff"/>
          <path d="M4.5 6l4.5 3.6L13.5 6" fill="none" stroke="var(--green)" stroke-width="1"/>
        </svg>
        Marcus@velturaq.com
      </li>
      <li class="contacts__item">
        <svg class="contacts__icon" viewBox="0 0 18 18" aria-hidden="true">
          <circle cx="9" cy="9" r="9" fill="var(--green)"/>
          <circle cx="9" cy="9" r="4.6" fill="none" stroke="#fff" stroke-width="1.2"/>
          <path d="M4.4 9h9.2M9 4.4c-2.4 2.6-2.4 6.6 0 9.2M9 4.4c2.4 2.6 2.4 6.6 0 9.2" fill="none" stroke="#fff" stroke-width="1"/>
        </svg>
        www.velturaq.com
      </li>
    </ul>

    <div class="accent-circle"></div>
    <div class="accent-tab"></div>
  </section>

  <section class="card card--back" aria-label="Card back">
    <div class="back-ring"></div>
    <div class="back-brand">
      <p class="back-brand__name">VELTURAQ</p>
      <p class="back-brand__tagline">CONTROLLED ENVIRONMENT AGRICULTURE</p>
    </div>
  </section>

</main>
</body>
</html>
```